Golf Tournament Flyer and Header Needed

Non-profit needs a flyer for their benefit golf tournament - "Wild Socks Charity Golf Classic"

Target Market(s)

Design and Construction industry professionals

Industry/Entity Type

Design and Construction

Colors

Designer to choose colors to be used in the design.

Requirements
Must have
• Date: September 22, 2021, 8:00 AM Shotgun Start, Location: Briarwood Links Club. U-DorMB Logo
Nice to have
• Would like image of golfers in crazy pants incorporated.

```html
<!DOCTYPE html>
<html lang="en">
<head>
<meta charset="utf-8">
<title>Wild Socks Charity Golf Classic – Flyer</title>
<link rel="stylesheet" href="https://fonts.googleapis.com/css2?family=Montserrat:ital,wght@0,500;0,600;0,700;0,800;1,600;1,700&display=swap">
<style>
  :root {
    --stage: #b2c1d2;
    --paper: #ffffff;
    --blue: #6677b6;
    --green: #9cc158;
    --ink: #333333;
    --photo-pink: #f0407a;
    --photo-teal: #6fd0c2;
    --photo-grass: #7fa45a;
  }
  * { box-sizing: border-box; margin: 0; padding: 0; }
  html, body { width: 1200px; height: 800px; overflow: hidden; }
  body {
    background: var(--stage);
    font-family: "Montserrat", Arial, sans-serif;
    display: flex; align-items: center; justify-content: center;
  }
  .flyer {
    position: relative;
    width: 540px; height: 760px;
    background: var(--paper);
    overflow: hidden;
    box-shadow: 0 10px 30px rgba(40, 55, 80, .25);
  }
  .flyer-art { position: absolute; inset: 0; }
  .headline {
    position: absolute; top: 60px; left: 110px; width: 380px;
    text-align: center; color: var(--green);
  }
  .headline-golf { font-size: 64px; font-weight: 800; letter-spacing: 4px; line-height: 1; }
  .headline-tournament {
    font-size: 11px; font-weight: 600; font-style: italic; color: var(--ink);
    letter-spacing: 9px; margin-top: 4px;
  }
  .headline-event { font-weight: 800; line-height: 1; margin-top: 12px; }
  .headline-event .line-small { font-size: 27px; display: block; }
  .headline-event .line-large { font-size: 33px; display: block; margin-top: 4px; }
  .details {
    position: absolute; top: 234px; left: 110px; width: 380px;
    text-align: center; color: var(--ink);
  }
  .details-date { font-size: 19px; font-weight: 700; line-height: 1.2; }
  .details-time { font-size: 16px; font-weight: 500; margin-top: 2px; line-height: 1.2; }
  .details-location { font-size: 15px; font-weight: 500; margin-top: 8px; line-height: 1.2; }
  .details-location .label { color: var(--green); font-weight: 700; font-style: italic; margin-right: 6px; }
  .host {
    position: absolute; top: 316px; left: 170px; width: 260px;
    text-align: center;
  }
  .host-name {
    font-size: 20px; font-weight: 700; color: var(--ink);
    letter-spacing: 3px; line-height: 1.2;
  }
</style>
</head>
<body>
  <main class="flyer">
    <svg class="flyer-art" width="540" height="760" viewBox="0 0 540 760">
      <defs>
        <linearGradient id="photo-tones" x1="0" y1="0" x2="0" y2="1">
          <stop offset="0" stop-color="#a9c79a"/>
          <stop offset=".35" stop-color="var(--photo-pink)"/>
          <stop offset=".7" stop-color="var(--photo-teal)"/>
          <stop offset="1" stop-color="var(--photo-grass)"/>
        </linearGradient>
      </defs>
      <path class="blob blob-top-left" fill="var(--blue)" d="M0,0 H230 C170,10 140,40 100,70 C60,100 40,140 0,160 Z"/>
      <path class="blob blob-top-right" fill="var(--blue)" d="M395,0 H540 V330 C505,320 470,300 480,250 C490,200 520,160 470,120 C420,90 380,60 395,0 Z"/>
      <path class="blob blob-left" fill="var(--blue)" d="M0,300 C40,270 90,250 105,285 C120,325 70,350 0,345 Z"/>
      <path class="blob blob-lower-right" fill="var(--blue)" d="M540,400 C490,410 430,420 425,480 C420,540 470,560 540,575 Z"/>
      <g class="dots dots-white" fill="#fff">
        <circle cx="470" cy="40" r="2"/><circle cx="490" cy="40" r="2"/><circle cx="510" cy="40" r="2"/><circle cx="530" cy="40" r="2"/>
        <circle cx="470" cy="58" r="2"/><circle cx="490" cy="58" r="2"/><circle cx="510" cy="58" r="2"/><circle cx="530" cy="58" r="2"/>
        <circle cx="470" cy="76" r="2"/><circle cx="490" cy="76" r="2"/><circle cx="510" cy="76" r="2"/><circle cx="530" cy="76" r="2"/>
        <circle cx="20" cy="300" r="2"/><circle cx="38" cy="300" r="2"/><circle cx="56" cy="300" r="2"/>
        <circle cx="20" cy="316" r="2"/><circle cx="38" cy="316" r="2"/><circle cx="56" cy="316" r="2"/><circle cx="74" cy="316" r="2"/>
      </g>
      <path class="squiggle" d="M90,250 q6,-6 12,0 t12,0 t12,0 t12,0" fill="none" stroke="var(--green)" stroke-width="2"/>
      <path class="cross" d="M258,52 h10 M263,47 v10" stroke="var(--green)" stroke-width="2"/>
      <circle class="accent-circle" cx="445" cy="395" r="32" fill="none" stroke="var(--green)" stroke-width="2"/>
      <circle class="accent-circle" cx="470" cy="415" r="32" fill="none" stroke="var(--green)" stroke-width="2"/>
      <path class="photo-band" fill="var(--green)" d="M0,345 C130,375 250,375 350,410 C460,455 490,620 400,700 C330,760 230,760 200,760 L0,760 Z"/>
      <path class="photo-area" role="img" aria-label="Photo of four golfers in matching bright pink polos, caps and sunglasses, wearing wild tropical flamingo-print trousers on a golf course" fill="url(#photo-tones)" d="M0,365 C120,395 240,387 330,420 C430,462 450,610 380,680 C320,740 230,750 180,760 L0,760 Z"/>
      <g class="dots dots-green" fill="var(--green)">
        <circle cx="420" cy="650" r="2.5"/><circle cx="440" cy="650" r="2.5"/><circle cx="460" cy="650" r="2.5"/><circle cx="480" cy="650" r="2.5"/>
        <circle cx="420" cy="670" r="2.5"/><circle cx="440" cy="670" r="2.5"/><circle cx="460" cy="670" r="2.5"/><circle cx="480" cy="670" r="2.5"/>
        <circle cx="420" cy="690" r="2.5"/><circle cx="440" cy="690" r="2.5"/><circle cx="460" cy="690" r="2.5"/><circle cx="480" cy="690" r="2.5"/>
        <circle cx="330" cy="720" r="2.5"/><circle cx="350" cy="720" r="2.5"/><circle cx="370" cy="720" r="2.5"/><circle cx="390" cy="720" r="2.5"/>
        <circle cx="330" cy="740" r="2.5"/><circle cx="350" cy="740" r="2.5"/><circle cx="370" cy="740" r="2.5"/><circle cx="390" cy="740" r="2.5"/>
      </g>
    </svg>

    <header class="headline">
      <div class="headline-golf">GOLF</div>
      <div class="headline-tournament">TOURNAMENT</div>
      <h1 class="headline-event">
        <span class="line-small">WILD SOCKS</span>
        <span class="line-large">CHARITY CLASSIC</span>
      </h1>
    </header>

    <section class="details">
      <p class="details-date">September 22, 2021</p>
      <p class="details-time">8:00 AM Shotgun Start</p>
      <p class="details-location"><span class="label">Location:</span>Briarwood Links Club.</p>
    </section>

    <div class="host">
      <span class="host-name">U-DORMB</span>
    </div>
  </main>
</body>
</html>
```